Vow-Garden-Officiants.com Rack Card Design, Double-Sided. See Attachments.

Please use the attached graphics and the contents of www.vow-garden-officiants.com to create a rack card that has the same look, feel and colors as the website, business card and existing logos. Your design must be consistent with how the business cards and website currently look.

Target Market(s)

weddings. Visit www.vow-garden-officiants.com for content and design ideas.

Requirements
Must have
• Same info as business card plus content from the website.

```html
<!DOCTYPE html>
<html lang="en">
<head>
<meta charset="utf-8">
<title>Vow-Garden-Officiants.com Rack Cards</title>
<link rel="stylesheet" href="https://fonts.googleapis.com/css2?family=Playfair+Display:wght@400;700;900&family=Lora:wght@400;700&family=Roboto:wght@400;700&family=Great+Vibes&display=swap">
<style>
:root{
  --bg:#d1d1d1;
  --taupe:#8c8474;
  --white:#ffffff;
  --ink:#3a3a3a;
  --line:#e9e6df;
}
*{margin:0;padding:0;box-sizing:border-box}
html,body{width:1200px;height:459px;overflow:hidden;background:var(--bg)}
.sheet{position:relative;width:1200px;height:459px}
.card{position:absolute;top:10px;width:199px;height:439px;background:var(--taupe);overflow:hidden;color:var(--white)}
.card > *{position:absolute}
.photo{left:0;width:199px}
.bouquet{background:linear-gradient(120deg,#d8d2cc 0%,#f1ece8 35%,#7d8a5f 55%,#e9e4dd 75%,#c9a9a4 100%)}
.field{background:linear-gradient(180deg,#c7cdd2 0%,#9ea6a6 35%,#6f7657 65%,#7c6c57 100%)}
.orchard{background:linear-gradient(180deg,#3f4a2b 0%,#5c6a38 45%,#8d9a5a 100%)}
.couple-dog{background:radial-gradient(ellipse at 60% 60%,#d9b98f 0%,#8f7a55 40%,#3e4a2e 100%)}
.reception{background:linear-gradient(135deg,#6b4a34,#c69c73,#e8d6bd)}
.sunset{background:linear-gradient(180deg,#4e5d6e 0%,#e07a2e 45%,#f4b04a 55%,#3b2b25 100%)}
.makeup{background:linear-gradient(135deg,#f2eeee,#c992a8,#8f5a6a)}
.gown{background:linear-gradient(135deg,#eae4dc,#ffffff,#b7a58c)}
.car{background:linear-gradient(135deg,#7aa0c2,#f4f1ec,#c9c6c0)}
.center{left:0;width:199px;text-align:center}
.rule{height:1px;background:var(--line);left:72px;width:55px}
.display{font-family:"Playfair Display",serif;font-weight:900;line-height:1}
.serif{font-family:"Lora",serif}
.sans{font-family:"Roboto",sans-serif}
.brandline{font-family:"Playfair Display",serif;font-weight:700;font-size:10px}
.tagline{font-family:"Lora",serif;font-size:8.6px}
.blurb{font-family:"Roboto",sans-serif;font-size:5.4px;line-height:7.4px}
.logo-name{font-family:"Lora",serif;font-size:7.6px;display:flex;justify-content:center;align-items:center;gap:4px}
.logo-name .dot{width:6px;height:6px;border:1px solid var(--white);border-radius:50%}
.contact{font-family:"Lora",serif;font-size:5.2px;line-height:7.4px}
.white-panel{left:0;width:199px;background:var(--white);color:var(--ink)}
.services-title{font-family:"Playfair Display",serif;font-weight:700;font-size:15px;color:var(--ink)}
.service-list{list-style:none;font-family:"Roboto",sans-serif;font-size:4.6px;line-height:11px}
.service-list li::before{content:"";display:inline-block;width:3px;height:3px;background:var(--ink);margin-right:2px;vertical-align:1px}
.service-list b{font-weight:700}
.centered-list{list-style:none;font-family:"Lora",serif;font-size:5px;line-height:11px;text-align:center}
.centered-list b{font-weight:700}
.script{font-family:"Great Vibes",cursive;font-size:7px;line-height:11px}
</style>
</head>
<body>
<main class="sheet">

  <!-- Card 1 -->
  <section class="card" style="left:72px">
    <div class="photo bouquet" style="top:0;height:95px" role="img" aria-label="Bride holding a white bouquet of flowers"></div>
    <div class="rule" style="top:110px"></div>
    <h1 class="center display" style="top:112px;font-size:26px">Your Wedding</h1>
    <p class="center sans" style="top:139px;font-size:10px;font-weight:400">starts here at</p>
    <p class="center brandline" style="top:151px">Marisol’s Vow-Garden-Officiants.com</p>
    <div class="rule" style="top:172px"></div>
    <p class="center tagline" style="top:176px">More Than Just a Marriage Officiant</p>
    <p class="center blurb" style="top:193px">I'll work day and night to guarantee that your next event<br>will be filled with unforgettable moments.</p>
    <div class="photo field" style="top:216px;height:151px" role="img" aria-label="Bride and groom running down a country path under a branch arch"></div>
    <p class="center logo-name" style="top:370px"><span class="dot"></span>Vow-Garden-Officiants.com</p>
    <p class="center contact" style="top:403px">214 Elm Street, Glastonbury, CT 06033<br>Marisol@Vow-Garden-Officiants.com<br>Marisol B. Castellano, (860) 555-0148<br>vow-garden-officiants.com</p>
  </section>

  <!-- Card 2 -->
  <section class="card" style="left:286px">
    <div class="photo bouquet" style="top:0;height:102px" role="img" aria-label="Bride holding a white bouquet of flowers"></div>
    <div class="rule" style="top:110px"></div>
    <h1 class="center display" style="top:114px;font-size:30px">Welcome</h1>
    <p class="center brandline" style="top:146px;font-size:9.4px">to Marisol’s Vow-Garden-Officiants.com</p>
    <p class="center tagline" style="top:164px">More Than Just a Marriage Officiant</p>
    <p class="center blurb" style="top:185px">I'll work day and night to guarantee that your next event<br>will be filled with unforgettable moments.</p>
    <div class="photo field" style="top:207px;height:160px" role="img" aria-label="Bride and groom running down a country path under a branch arch"></div>
    <p class="center logo-name" style="top:370px"><span class="dot"></span>Vow-Garden-Officiants.com</p>
    <p class="center contact" style="top:403px">214 Elm Street, Glastonbury, CT 06033<br>Marisol@Vow-Garden-Officiants.com<br>Marisol B. Castellano, (860) 555-0148<br>vow-garden-officiants.com</p>
  </section>

  <!-- Card 3 -->
  <section class="card" style="left:501px">
    <div class="photo field" style="top:0;height:140px" role="img" aria-label="Bride and groom running down a country path under a branch arch"></div>
    <p class="center logo-name" style="top:152px"><span class="dot"></span>Vow-Garden-Officiants.com</p>
    <div class="rule" style="top:184px;left:62px;width:75px"></div>
    <h1 class="center display" style="top:189px;font-size:30px">Welcome</h1>
    <p class="center brandline" style="top:220px;font-size:9.4px">to Marisol’s Vow-Garden-Officiants.com</p>
    <p class="center tagline" style="top:248px;font-size:9px">More Than Just a Marriage Officiant</p>
    <div class="photo couple-dog" style="top:266px;height:112px" role="img" aria-label="Couple in flower crowns hugging their dog outdoors"></div>
    <p class="center serif" style="top:384px;font-size:6.8px;line-height:12.4px">I’ll work day and night to guarantee<br>that your next event will be filled with<br>unforgettable moments.</p>
  </section>

  <!-- Card 4 -->
  <section class="card" style="left:716px">
    <div class="photo orchard" style="top:0;height:96px" role="img" aria-label="Bride and groom walking hand in hand through an orchard"></div>
    <div class="photo bouquet" style="top:96px;height:82px;width:108px" role="img" aria-label="Bride holding a white bouquet of flowers"></div>
    <p class="serif" style="left:108px;top:101px;width:91px;text-align:center;font-size:9.4px;line-height:11px">We have everything<br>for your dream day –</p>
    <p class="script" style="left:108px;top:124px;width:91px;text-align:center">offering you a Network of<br>Professional Service Providers<br>Who Can Assist with Your Whole<br>Special Occasion!</p>
    <div class="white-panel" style="top:178px;height:261px"></div>
    <h2 class="services-title" style="left:18px;top:181px">Our Event Services:</h2>
    <ul class="service-list" style="left:18px;top:198px;color:var(--ink)">
      <li><b>Floral Arrangement Coordination</b> – Perfectly Planned</li>
      <li><b>Professional Photographer Coordination</b> – Stunning and Memorable</li>
      <li><b>Hair &amp; Makeup Coordination</b> – Timely &amp; Convenient</li>
      <li><b>From Here to There to There</b> – Classy, Luxurious and Convenient.</li>
      <li><b>Coordination of Small Receptions</b> – Restaurants &amp; Wineries</li>
      <li><b>You Can Event Sail Away!</b> – Charters by Captain Dean Halloway</li>
    </ul>
    <div class="photo reception" style="top:266px;height:61px;width:99px" role="img" aria-label="Decorated reception tables in a rustic hall"></div>
    <div class="photo sunset" style="top:266px;left:99px;height:61px;width:100px" role="img" aria-label="Boat on a lake at sunset"></div>
    <div class="photo makeup" style="top:327px;height:62px;width:99px" role="img" aria-label="Makeup compact and pink tulips"></div>
    <div class="photo gown" style="top:327px;left:99px;height:62px;width:100px" role="img" aria-label="Bride in a flowing gown on a beach"></div>
    <p class="center contact" style="top:394px;color:var(--ink);font-size:5.4px">Contact:<br>214 Elm Street, Glastonbury, CT 06033<br>Marisol@Vow-Garden-Officiants.com<br>Marisol B. Castellano, (860) 555-0148<br>vow-garden-officiants.com</p>
  </section>

  <!-- Card 5 -->
  <section class="card" style="left:930px">
    <div class="photo bouquet" style="top:0;left:26px;width:145px;height:82px" role="img" aria-label="Bride holding a white bouquet of flowers"></div>
    <p class="center serif" style="top:90px;font-size:5.8px;line-height:11px">We have everything for your dream day – offering<br>you a Network of Professional Service Providers Who<br>Can Assist with Your Whole Special Occasion!</p>
    <div class="photo orchard" style="top:127px;left:26px;width:145px;height:83px" role="img" aria-label="Bride and groom walking hand in hand through an orchard"></div>
    <p class="center serif" style="top:213px;font-size:5.2px;line-height:11px">Reduce Your Stress and Save Time.<br>Let’s Use My Network of Professional Providers.</p>
    <h2 class="center services-title" style="top:249px;color:var(--white)">Our Event Services:</h2>
    <div class="white-panel" style="top:262px;height:177px"></div>
    <ul class="centered-list" style="left:0;width:199px;top:266px;color:var(--ink)">
      <li><b>Floral Arrangement Coordination</b> – Perfectly Planned</li>
      <li><b>Professional Photographer Coordination</b> – Stunning and Memorable</li>
      <li><b>Hair &amp; Makeup Coordination</b> – Timely &amp; Convenient</li>
      <li><b>From Here to There to There.</b> – Classy, Luxurious and Convenient.</li>
      <li><b>Coordination of Small Receptions.</b> – Restaurants &amp; Wineries</li>
      <li><b>You Can Event Sail Away!</b> – Charters by Captain Dean Halloway</li>
    </ul>
    <div class="photo makeup" style="top:339px;width:73px;height:49px" role="img" aria-label="Makeup compact and pink tulips"></div>
    <div class="photo car" style="top:339px;left:73px;width:58px;height:49px" role="img" aria-label="Bride holding a bouquet out of a car window"></div>
    <div class="photo sunset" style="top:339px;left:131px;width:68px;height:49px" role="img" aria-label="Boat on a lake at sunset"></div>
    <p class="center contact" style="top:395px;color:var(--ink);font-size:5.4px;line-height:6.8px">Contact:<br>214 Elm Street, Glastonbury, CT 06033<br>Marisol@Vow-Garden-Officiants.com<br>Marisol B. Castellano, (860) 555-0148<br>vow-garden-officiants.com</p>
  </section>

</main>
</body>
</html>
```